Pinecrest Fitness

I am looking for a crisp/clean website That is simple. We are looking for membership page, about us, photos, and retail sale of out clothes and accessories.

Below is our logo.

Industry/Entity Type

Retail

Number of Pages Required

4 page

Font styles to use
Sans Serif

```html
<!DOCTYPE html>
<html lang="en">
<head>
<meta charset="utf-8">
<title>Pinecrest Fitness</title>
<link href="https://fonts.googleapis.com/css2?family=Saira:wght@400;500&family=Arimo:wght@400&display=swap" rel="stylesheet">
<style>
  :root{
    --red:#c0201a;
    --red-bright:#e0251c;
    --ink:#1c1c1c;
    --header-bg:#dedede;
    --page-dark:#2a2a2a;
    --panel:#f4f4f4;
    --card:#ffffff;
    --line:#d8d8d8;
    --light-text:#f2f2f2;
  }
  *{box-sizing:border-box;margin:0;padding:0}
  html,body{width:1043px;height:1200px;overflow:hidden;background:var(--page-dark)}
  body{font-family:"Saira",sans-serif;color:var(--ink)}
  .site{position:relative;width:1043px;height:1200px;overflow:hidden;
    background:repeating-linear-gradient(45deg,#2d2d2d 0 2px,#262626 2px 4px)}
  .abs{position:absolute}

  /* header */
  .header{left:0;top:0;width:1043px;height:109px;
    background:repeating-linear-gradient(90deg,#e2e2e2 0 2px,#d9d9d9 2px 4px)}
  .brand{left:69px;top:36px;display:flex;align-items:center;gap:10px;
    font-size:30px;font-weight:500;color:var(--ink);letter-spacing:.5px}
  .brand-mark{width:22px;height:22px;background:var(--red)}
  .nav a{position:absolute;top:40px;font-size:16.5px;color:var(--ink);text-decoration:none;letter-spacing:.3px}
  .nav a.active{color:var(--red)}
  .nav-marker{left:437px;top:0;width:90px;height:5px;background:var(--red)}
  .nav-marker::after{content:"";position:absolute;left:39px;top:5px;border:6px solid transparent;border-top-color:var(--red)}

  /* hero */
  .hero{left:0;top:109px;width:1043px;height:298px;
    background:linear-gradient(90deg,#3a3a3a 0%,#4a4a4a 40%,#2c2c2c 100%)}
  .hero-photo{left:470px;top:109px;width:573px;height:298px;
    background:radial-gradient(ellipse at 45% 55%,#a06a4c 0%,#6e4634 35%,#3a2e2a 70%,#2b2b2b 100%)}
  .hero-panel{left:135px;top:170px;width:391px;height:172px;background:rgba(222,222,222,.93);overflow:hidden}
  .hero-panel svg{position:absolute;left:0;top:0}
  .hero-title{position:absolute;left:60px;top:24px;width:300px;text-align:center;
    font-size:38px;line-height:45px;color:var(--red);font-weight:400}

  /* content */
  .content{left:67px;top:381px;width:909px;height:560px;background:var(--panel)}
  .promo{left:81px;top:395px;width:879px;height:126px;
    background:linear-gradient(90deg,#c9c5c6 0%,#bdbac0 60%,#c8c6cb 100%)}
  .promo-photo{left:81px;top:395px;width:281px;height:126px;
    background:linear-gradient(90deg,#9c8a7c,#cbb7a8 60%,#b6aca6)}
  .promo-title{left:369px;top:397px;font-size:31px;color:var(--red);letter-spacing:.2px;white-space:nowrap}
  .promo-text{left:369px;top:437px;width:540px;font-size:16px;line-height:20px;color:var(--ink)}
  .btn{display:flex;align-items:center;justify-content:center;gap:10px;background:var(--red);color:#fff;
    font-size:17px;letter-spacing:.3px}
  .promo-btn{left:369px;top:484px;width:109px;height:29px}

  .section-title{left:0;top:538px;width:1043px;text-align:center;font-size:25px;color:var(--red);letter-spacing:.5px}

  .card{top:590px;width:209px;height:292px;background:var(--card);box-shadow:0 1px 3px rgba(0,0,0,.25)}
  .card-photo{position:absolute;left:7px;top:7px;width:195px;height:163px;background:linear-gradient(180deg,#f0f0f0,#e4e4e4)}
  .card-name{position:absolute;left:0;top:180px;width:209px;text-align:center;font-size:14.5px;line-height:15px;color:var(--red)}
  .card-price{position:absolute;left:0;top:216px;width:209px;text-align:center;font-size:16px;color:var(--ink)}
  .card .btn{position:absolute;left:28px;top:248px;width:142px;height:32px;font-size:16.5px}

  /* footer */
  .footer-title{font-size:22px;color:var(--red-bright);letter-spacing:.3px}
  .links a{position:absolute;font-size:14.5px;color:var(--light-text);text-decoration:none}
  .newsletter-text{left:349px;top:986px;width:290px;font-size:14.5px;line-height:20px;color:var(--light-text)}
  .email{left:350px;top:1034px;width:261px;height:26px;background:#fff;font-family:"Arimo",sans-serif;
    font-size:11.5px;color:#888;padding:6px 8px}
  .subscribe{left:350px;top:1075px;width:109px;height:27px;font-size:16px}
  .footer-photo{left:690px;top:946px;width:260px;height:226px;border-radius:40% 40% 30% 30%;
    background:radial-gradient(ellipse at 50% 55%,#7a5a4c 0%,#4a3a36 50%,rgba(42,42,42,0) 75%)}
  .copyright{left:0;top:1151px;width:1043px;text-align:center;font-family:"Arimo",sans-serif;font-size:11.5px;color:var(--light-text)}
  .copyright span{color:var(--red-bright);text-decoration:underline}
</style>
</head>
<body>
<div class="site">
  <header class="header abs">
    <div class="brand abs"><span class="brand-mark"></span>Pinecrest Fitness</div>
    <div class="nav-marker abs"></div>
    <nav class="nav">
      <a class="active" style="left:460px">Home</a>
      <a style="left:568px">About Us</a>
      <a style="left:697px">Photo</a>
      <a style="left:802px">Shop</a>
      <a style="left:901px">Contact</a>
    </nav>
  </header>

  <section class="hero abs"></section>
  <div class="hero-photo abs" role="img" aria-label="Athletic woman in a sports bra lifting red dumbbells"></div>
  <div class="hero-panel abs">
    <svg width="391" height="172" viewBox="0 0 391 172">
      <polygon points="0,0 0,172 100,172" fill="#c0201a"/>
      <polygon points="350,0 391,0 391,70" fill="#c0201a"/>
    </svg>
    <h1 class="hero-title">GET IN YOUR BEST SHAPE NOW!</h1>
  </div>

  <main class="content abs"></main>
  <div class="promo abs"></div>
  <div class="promo-photo abs" role="img" aria-label="Woman stretching during a workout with earphones"></div>
  <h2 class="promo-title abs">GET BETTER RESULTS &amp; A TON OF FUN</h2>
  <p class="promo-text abs">Lorem Ipsum simply dummy text of the printing and typesetting industry.</p>
  <div class="promo-btn btn abs">Retail Sale</div>

  <h2 class="section-title abs">HOT PRODUCTS</h2>

  <div class="card abs" style="left:81px">
    <div class="card-photo" role="img" aria-label="Woman in a mint sports bra and shorts"></div>
    <p class="card-name">Fitness clothing female<br>aerobics clothes</p>
    <p class="card-price">$ 23.00</p>
    <div class="btn">Add to Cart <svg width="20" height="18" viewBox="0 0 20 18"><path d="M0 2h4l3 10h10l2-7H6" fill="none" stroke="#fff" stroke-width="2.4"/><circle cx="8" cy="16" r="1.8" fill="#fff"/><circle cx="16" cy="16" r="1.8" fill="#fff"/></svg></div>
  </div>
  <div class="card abs" style="left:304px">
    <div class="card-photo" role="img" aria-label="Two women in tank tops and capri leggings"></div>
    <p class="card-name">Fitness clothing female<br>aerobics clothes</p>
    <p class="card-price">$ 23.00</p>
    <div class="btn">Add to Cart <svg width="20" height="18" viewBox="0 0 20 18"><path d="M0 2h4l3 10h10l2-7H6" fill="none" stroke="#fff" stroke-width="2.4"/><circle cx="8" cy="16" r="1.8" fill="#fff"/><circle cx="16" cy="16" r="1.8" fill="#fff"/></svg></div>
  </div>
  <div class="card abs" style="left:529px">
    <div class="card-photo" role="img" aria-label="Man in black training shirt and shorts"></div>
    <p class="card-name">Fitness clothing female<br>aerobics clothes</p>
    <p class="card-price">$ 23.00</p>
    <div class="btn">Add to Cart <svg width="20" height="18" viewBox="0 0 20 18"><path d="M0 2h4l3 10h10l2-7H6" fill="none" stroke="#fff" stroke-width="2.4"/><circle cx="8" cy="16" r="1.8" fill="#fff"/><circle cx="16" cy="16" r="1.8" fill="#fff"/></svg></div>
  </div>
  <div class="card abs" style="left:754px">
    <div class="card-photo" role="img" aria-label="Woman in red top and black yoga pants"></div>
    <p class="card-name">Fitness clothing female<br>aerobics clothes</p>
    <p class="card-price">$ 23.00</p>
    <div class="btn">Add to Cart <svg width="20" height="18" viewBox="0 0 20 18"><path d="M0 2h4l3 10h10l2-7H6" fill="none" stroke="#fff" stroke-width="2.4"/><circle cx="8" cy="16" r="1.8" fill="#fff"/><circle cx="16" cy="16" r="1.8" fill="#fff"/></svg></div>
  </div>

  <footer>
    <h3 class="footer-title abs" style="left:78px;top:958px">USEFUL LINK</h3>
    <nav class="links">
      <a style="left:81px;top:992px">Home</a>
      <a style="left:81px;top:1015px">About Us</a>
      <a style="left:81px;top:1039px">Photo</a>
      <a style="left:81px;top:1062px">Shop</a>
      <a style="left:81px;top:1086px">Contact</a>
      <a style="left:198px;top:992px">Help</a>
      <a style="left:198px;top:1015px">Community</a>
      <a style="left:198px;top:1039px">FAQ</a>
      <a style="left:198px;top:1062px">Privacy Policy</a>
      <a style="left:198px;top:1086px">Terms &amp; Condition</a>
    </nav>
    <h3 class="footer-title abs" style="left:349px;top:958px">Subscribe to Newsletter</h3>
    <p class="newsletter-text abs">Get to know the latest new and offers we provide on this site. we don't spam</p>
    <div class="email abs">Enter your Email</div>
    <div class="subscribe btn abs">Subscribe</div>
    <div class="footer-photo abs" role="img" aria-label="Woman sitting cross-legged listening to music on her phone"></div>
    <p class="copyright abs">© <span>Pinecrest Fitness</span> - 2014. All Rights Reserved.</p>
  </footer>
</div>
</body>
</html>
```